Home Page Design for Motor Manufacturer

Hello,
please design the homepage for a manufacturer of industry motors. I am looking for a professional, clean and minimalistic design. Since this a rather conservative industry it should get a professional look but since it is a redesign there should be some modern that gives is the modern touch of innovation.
A competitor's homepage I like is:
https://www.valtrosen.com/en/
What I like about this website:
* clean, minimal, well structured design
* mega menu
For this project please find attached the wireframes (most buttons are in German but by context and Google translate you will easily figure it out; only unclear - "Messe" means "trade exhibition"). The paddings and margins are NOT exact. Also any color of backgrounds etc. chosen is not meant to represent a real color but rather to illustrate the object and maybe show there should be some background emphasis (color or image).
Wireframes:
https: //www.filquarry. com / t / pWmeTuZa8LkiBvQx
In both wireframes the only thing that is different is the Service section. I expect from the winner both designs for this service section: one with normal cart design and one with tabs as filters to search products (find image for product categories attached)
In the header use on the left the following text:
h1: "Your competent partner for industrial engines,
-transmission and drawing parts
with more than 5000 satisfied customers "
primary button: Our products
sec. button: Download catalog
and on the right side we feature one or more product images (like putting them in a nice display together).
I also think of a solid background color or subtle gradient for the hero section.
The winner should also design an open mega menu version.
Menu items in this order:
• Home page
• Gearboxes & Motors
• Engine components
• Drawing parts
• Machines & accessories
• About us
• Contact
Also create a language switch with globe symbol and DE for Germany and EN for English above the nav plus the telephone number with icon (user dummy number +49 (0) 987650432)
Output should be in Figma, Sketch or PSD.
Fonts + color to use:
header: Proza Libre, bold, # 0171A1
body: Open Sans, regular, black
Primary accent color: # 0171A1
Text black or dark gray
background: light gray, white or shade of blue
More image resources:
https://www.filquarry.com/t/RnaHwoqPEdLu5sjv
If there are any questions please do not hesitate to ask.
Target Market(s)
B2B - anyone with industrial machinery needing small motors (not car engines)
Industry/Entity Type
Manufacturing
Number of Pages Required
1 page
Requirements
Must have
- see above
Nice to have
- see above
Should not have
- see above

```html
<!DOCTYPE html>
<html lang="en">
<head>
<meta charset="utf-8">
<title>Orvane – Industrial Engines</title>
<link href="https://fonts.googleapis.com/css2?family=Proza+Libre:wght@400;500;600;700&family=Open+Sans:wght@400;600;700&display=swap" rel="stylesheet">
<style>
:root{
  --accent:#0171a1;
  --accent-dark:#0d4d73;
  --navy:#0a3d5e;
  --ink:#222;
  --muted:#555;
  --light:#f3f3f3;
  --topbar:#efefef;
  --white:#fff;
}
*{margin:0;padding:0;box-sizing:border-box}
html,body{width:1200px;height:4071px;overflow:hidden}
body{position:relative;font-family:"Open Sans",sans-serif;color:var(--ink);background:var(--white)}
.abs{position:absolute}
.heading{font-family:"Proza Libre",sans-serif}
/* top bar */
.topbar{left:0;top:0;width:1200px;height:71px;background:var(--topbar)}
.brand{left:120px;top:14px;font-family:"Proza Libre",sans-serif;font-weight:700;font-size:38px;color:var(--accent);letter-spacing:1px}
.lang{left:822px;top:24px;width:70px;height:28px;border:1px solid #ddd;background:#fff;border-radius:3px;display:flex;align-items:center;justify-content:space-around;font-size:13px;color:var(--muted)}
.phone-top{left:917px;top:26px;display:flex;align-items:center;gap:12px;font-size:15px;color:#333}
.phone-top .ring{width:26px;height:26px;border:1px solid #bbb;border-radius:50%;display:flex;align-items:center;justify-content:center}
/* nav */
.nav{left:0;top:71px;width:1200px;height:57px;background:#fff;border-bottom:2px solid #d8d8d8}
.nav a{position:absolute;top:18px;font-size:15.5px;color:#333;text-decoration:none}
.nav a.active{color:var(--accent)}
.nav .caret{display:inline-block;margin-left:6px;border:4px solid transparent;border-top-color:#888;vertical-align:-1px}
/* hero */
.hero{left:0;top:128px;width:1200px;height:620px;background:linear-gradient(180deg,#0173a3 0%,#0a6b9a 55%,#05618f 100%)}
.hero h1{left:120px;top:166px;width:520px;font-family:"Proza Libre",sans-serif;font-weight:700;font-size:38px;line-height:52px;color:#fff}
.hero p{left:120px;top:295px;font-size:21.5px;line-height:35px;color:#fff}
.btn-pill{left:122px;top:395px;width:150px;height:38px;border-radius:19px;background:#1a9ac6;color:#fff;font-size:17px;display:flex;align-items:center;justify-content:center}
.hero-ring{left:637px;top:98px;width:376px;height:376px;border-radius:50%;background:#0b87b8}
.hero-disc{left:648px;top:109px;width:354px;height:354px;border-radius:50%;background:#fff;border:6px solid #e9f4f8}
.hero-photo{left:684px;top:150px;width:290px;height:260px;border-radius:40%;background:radial-gradient(ellipse at 55% 50%,#2a3a48 0%,#6f7a83 45%,#d9dee2 75%,#fff 100%)}
.thumb{width:60px;height:60px;border-radius:50%;border:3px solid #fff;background:radial-gradient(circle,#5f7584,#c8d3da)}
.hero-wave{left:0;top:700px;width:1200px;height:50px}
/* why */
.section-title{width:1200px;left:0;text-align:center;font-family:"Proza Libre",sans-serif;font-weight:500;font-size:44px;color:#222}
.why-text{left:250px;top:883px;width:700px;text-align:center;font-size:14.5px;line-height:27.5px;color:#333}
.feature{display:flex;align-items:center;gap:18px}
.feature .icon{width:96px;height:96px;border-radius:50%;border:2px solid #1a9ac6;display:flex;align-items:center;justify-content:center}
.feature .icon span{width:82px;height:82px;border-radius:50%;background:var(--accent);display:flex;align-items:center;justify-content:center}
.feature div.label{font-family:"Proza Libre",sans-serif;font-size:21px;line-height:27px;color:#333}
/* products */
.products{left:0;top:1213px;width:1200px;height:871px;background:linear-gradient(90deg,#2a2a2c 0%,#5a4c45 25%,#8e8277 45%,#6c5a4e 65%,#3a3634 85%,#2b2b2d 100%)}
.card{position:absolute;width:300px;height:256px;background:#fff;text-align:center}
.card.featured{background:var(--accent)}
.card .img{position:absolute;left:70px;top:24px;width:160px;height:140px;border-radius:8px;background:radial-gradient(ellipse,#3c4550 0%,#9aa4ac 55%,transparent 75%)}
.card .name{position:absolute;left:0;width:100%;top:188px;font-family:"Proza Libre",sans-serif;font-size:19px;color:#222}
.card.featured .name{color:#fff}
.pill{position:absolute;left:95px;bottom:-14px;width:110px;height:28px;border-radius:14px;background:#8a8a8a;color:#fff;font-size:14px;line-height:28px}
.card.featured .pill{background:var(--navy)}
.btn-dark{width:154px;height:48px;background:var(--navy);color:#fff;font-size:19px;display:flex;align-items:center;justify-content:center;font-family:"Proza Libre",sans-serif}
/* trade */
.trade{position:absolute;width:302px;height:398px;background:var(--light)}
.trade .photo{position:absolute;left:0;width:302px;height:199px}
.trade .body{position:absolute;left:29px;width:240px}
.trade h3{font-family:"Proza Libre",sans-serif;font-weight:500;font-size:17px;color:#222;margin-bottom:12px}
.trade p{font-size:13px;line-height:24px;color:#444}
.trade .btns{display:flex;gap:14px;margin-top:20px}
.trade .btns span{height:30px;padding:0 15px;line-height:30px;font-size:14px;color:#fff;background:var(--accent)}
.trade .btns span.alt{background:var(--navy)}
/* ebook */
.ebook{left:0;top:2903px;width:1200px;height:196px;background:var(--accent)}
.ebook h2{left:463px;top:32px;font-family:"Proza Libre",sans-serif;font-weight:500;font-size:34px;color:#fff}
.ebook p{left:463px;top:83px;font-size:17px;color:#e6f3f9}
.ebook .dl{left:462px;top:122px;width:168px;height:42px;border-radius:21px;background:#111;color:#fff;font-size:14px;font-weight:600;display:flex;align-items:center;justify-content:center}
/* about */
.about{left:0;top:3189px;width:1200px;height:547px;background:linear-gradient(110deg,#e9ecef 0%,#c98a45 25%,#d77a2a 40%,#8a8f96 60%,#3b4248 80%,#c6ccd1 100%)}
.about-box{left:337px;top:3295px;width:528px;height:313px;background:#fff;border:2px solid var(--accent);padding:34px 54px}
.about-box h2{font-family:"Proza Libre",sans-serif;font-weight:500;font-size:38px;color:#222;margin-bottom:20px}
.about-box p{font-size:14.5px;line-height:25.5px;color:#444;margin-bottom:20px}
/* footer */
.footer{left:0;top:3736px;width:1200px;height:256px;background:var(--accent);color:#fff}
.footer .f-brand{left:120px;top:54px;font-family:"Proza Libre",sans-serif;font-weight:700;font-size:66px;line-height:80px;letter-spacing:2px}
.footer h4{font-family:"Proza Libre",sans-serif;font-weight:500;font-size:16px}
.footer .col{font-size:13.5px;line-height:24px}
.footer .row{display:flex;gap:14px;align-items:flex-start;margin-bottom:10px}
.soc{width:20px;height:20px;border:2px solid #fff;border-radius:50%}
.contact-now{left:862px;top:174px;width:177px;height:44px;background:var(--navy);border-radius:22px;display:flex;align-items:center;gap:16px;padding-left:6px;font-size:15px}
.contact-now span.ic{width:34px;height:34px;border-radius:50%;border:1.5px solid #fff;display:flex;align-items:center;justify-content:center}
.bottombar{left:0;top:3992px;width:1200px;height:79px;background:#05628f;color:#fff;font-size:15px}
</style>
</head>
<body>

<header>
  <div class="abs topbar"></div>
  <div class="abs brand">Orvane</div>
  <div class="abs lang"><span>EN</span><span>&#9662;</span></div>
  <div class="abs phone-top">
    <span class="ring"><svg width="14" height="14" viewBox="0 0 24 24"><path d="M6.6 10.8a15 15 0 006.6 6.6l2.2-2.2a1 1 0 011-.25 11.4 11.4 0 003.6.57 1 1 0 011 1V20a1 1 0 01-1 1A17 17 0 013 4a1 1 0 011-1h3.5a1 1 0 011 1c0 1.25.2 2.45.57 3.57a1 1 0 01-.25 1z" fill="none" stroke="#777" stroke-width="1.6"/></svg></span>
    <span>+49 (0) 987650432</span>
  </div>
  <nav class="abs nav">
    <a class="active" style="left:119px">Home</a>
    <a style="left:193px">Gearboxes &amp; Motors<i class="caret"></i></a>
    <a style="left:384px">Engine Components<i class="caret"></i></a>
    <a style="left:574px">Drawing parts<i class="caret"></i></a>
    <a style="left:719px">Machines &amp; Accessories<i class="caret"></i></a>
    <a style="left:931px">About Us</a>
    <a style="left:1026px">Contact</a>
  </nav>
</header>

<section class="abs hero">
  <h1 class="abs">Your Competent Partner For Industrial Engines</h1>
  <p class="abs">Transmission And Drawing Parts<br>With More Than 5000 Satisfied Customers</p>
  <div class="abs btn-pill">Learn More</div>
  <div class="abs hero-ring"></div>
  <div class="abs hero-disc"></div>
  <div class="abs hero-photo" role="img" aria-label="Planetary gear motor product photo"></div>
  <svg class="abs" style="left:1048px;top:143px" width="22" height="14" viewBox="0 0 22 14"><path d="M2 12l9-9 9 9" fill="none" stroke="#7fc1dc" stroke-width="2"/></svg>
  <div class="abs thumb" style="left:1029px;top:183px" role="img" aria-label="Angle gearbox thumbnail"></div>
  <div class="abs thumb" style="left:1025px;top:259px;width:68px;height:68px;background:radial-gradient(circle,#2c3d4b,#b8c8d2)" role="img" aria-label="Gear motor thumbnail"></div>
  <div class="abs thumb" style="left:1029px;top:342px" role="img" aria-label="Motor thumbnail"></div>
  <svg class="abs" style="left:1048px;top:400px" width="22" height="14" viewBox="0 0 22 14"><path d="M2 2l9 9 9-9" fill="none" stroke="#7fc1dc" stroke-width="2"/></svg>
</section>
<svg class="abs hero-wave" viewBox="0 0 1200 50" preserveAspectRatio="none"><path d="M0 50 Q600 -20 1200 40 L1200 50 Z" fill="#fff"/></svg>

<section>
  <h2 class="abs section-title" style="top:808px">Why Choose Us</h2>
  <p class="abs why-text">Lorem Ipsum is simply dummy text of the printing and typesetting industry. Lorem Ipsum has been the industry's standard dummy text ever since the 1500s Lorem Ipsum is simply dummy text of the printing and typesetting industry.</p>
  <div class="abs feature" style="left:194px;top:1009px">
    <div class="icon"><span><svg width="44" height="44" viewBox="0 0 44 44" fill="none" stroke="#fff" stroke-width="2.5"><circle cx="22" cy="13" r="7"/><path d="M9 30c2-7 24-7 26 0"/><path d="M8 38l2-4 2 4-3-2h2zM20 38l2-4 2 4M32 38l2-4 2 4"/></svg></span></div>
    <div class="label">Customer<br>Satisfaction</div>
  </div>
  <div class="abs feature" style="left:489px;top:1009px">
    <div class="icon"><span><svg width="44" height="44" viewBox="0 0 44 44" fill="none" stroke="#fff" stroke-width="2.5"><circle cx="22" cy="22" r="16"/><circle cx="22" cy="22" r="11"/><path d="M26 17c-1-2-7-2-7 1s7 2 7 6-6 3-7 1M22 13v18"/></svg></span></div>
    <div class="label">Optimal<br>Price</div>
  </div>
  <div class="abs feature" style="left:768px;top:1009px">
    <div class="icon"><span><svg width="44" height="44" viewBox="0 0 44 44" fill="none" stroke="#fff" stroke-width="2.5"><circle cx="22" cy="18" r="11"/><path d="M22 12l2 4 4 .5-3 3 .8 4-3.8-2-3.8 2 .8-4-3-3 4-.5z"/><path d="M14 27l-5 10 6-1 3 4 4-9M30 27l5 10-6-1-3 4-4-9"/></svg></span></div>
    <div class="label">High Quality<br>Performance</div>
  </div>
</section>

<section class="abs products" role="img" aria-label="Blurred factory interior background">
</section>
<h2 class="abs section-title" style="top:1274px;color:#fff">Our Products</h2>
<div class="card" style="left:130px;top:1513px"><div class="img" role="img" aria-label="Planetary gearhead photo"></div><div class="name">Product Category</div><div class="pill">Details</div></div>
<div class="card featured" style="left:451px;top:1374px"><div class="img" style="background:radial-gradient(ellipse,#e6e9ec 0%,#7d8a95 45%,transparent 75%)" role="img" aria-label="Right angle gearbox photo"></div><div class="name">Product Category</div><div class="pill">Details</div></div>
<div class="card" style="left:451px;top:1665px"><div class="img" style="background:radial-gradient(circle,#6b7178 0%,#c5c9cd 45%,transparent 72%)" role="img" aria-label="Cycloidal reducer photo"></div><div class="name">Product Category</div><div class="pill">Details</div></div>
<div class="card" style="left:772px;top:1513px"><div class="img" style="background:radial-gradient(ellipse,#2f3a44 0%,#8a95a0 50%,transparent 75%)" role="img" aria-label="Gear motor photo"></div><div class="name">Product Category</div><div class="pill">Details</div></div>
<div class="abs btn-dark" style="left:523px;top:1979px">View More</div>

<section>
  <h2 class="abs section-title" style="top:2215px">Trade Exhibition</h2>
  <div class="trade" style="left:133px;top:2310px">
    <div class="photo" style="top:0;background:linear-gradient(135deg,#7b6a5a,#3b5da8 50%,#22305a)" role="img" aria-label="Crowded trade fair hall"></div>
    <div class="body" style="top:220px"><h3>Trade Exhibition</h3><p>Lorem Ipsum is simply dummy text of the printing and typesetting industry.</p><div class="btns"><span>Free tickets</span><span class="alt">Details</span></div></div>
  </div>
  <div class="trade" style="left:451px;top:2310px">
    <div class="body" style="top:22px"><h3>Trade Exhibition</h3><p>Lorem Ipsum is simply dummy text of the printing and typesetting industry.</p><div class="btns"><span>Free tickets</span><span class="alt">Details</span></div></div>
    <div class="photo" style="top:199px;background:linear-gradient(160deg,#c9d6e8,#2c5a9c 45%,#1b2c48)" role="img" aria-label="Visitors at an exhibition stand"></div>
  </div>
  <div class="trade" style="left:768px;top:2310px">
    <div class="photo" style="top:0;background:linear-gradient(135deg,#1d2a3a,#4a7a5c 45%,#b8c4b8 70%,#233046)" role="img" aria-label="Exhibition booth with green lighting"></div>
    <div class="body" style="top:220px"><h3>Trade Exhibition</h3><p>Lorem Ipsum is simply dummy text of the printing and typesetting industry.</p><div class="btns"><span>Free tickets</span><span class="alt">Details</span></div></div>
  </div>
  <div class="abs btn-dark" style="left:523px;top:2759px">View More</div>
</section>

<section class="abs ebook">
  <svg class="abs" style="left:0;top:0" width="420" height="196" viewBox="0 0 420 196">
    <path d="M0 0H330L378 98 330 196H0Z" fill="#e4eef3"/>
    <path d="M200 12H318L376 98 318 184H200L148 98Z" fill="#fff"/>
    <path d="M210 22H308L362 98 308 174H210L162 98Z" fill="var(--navy)"/>
    <g fill="none" stroke="#fff" stroke-width="2.2"><rect x="246" y="45" width="26" height="40" rx="3"/><rect x="262" y="52" width="18" height="14"/><path d="M266 56h10M266 60h10"/><path d="M252 80h6"/></g>
    <text x="261" y="124" text-anchor="middle" font-family="Proza Libre, sans-serif" font-size="25" fill="#fff">Ebook</text>
  </svg>
  <h2 class="abs">Lorem Ipsum is simply dummy text</h2>
  <p class="abs">Lorem Ipsum has been the industry's standard dummy</p>
  <div class="abs dl">Download Now</div>
</section>

<section>
  <div class="abs about" role="img" aria-label="Orange robotic arm with a tablet in a factory"></div>
  <div class="abs about-box">
    <h2>About Us</h2>
    <p>Lorem Ipsum is simply dummy text of the printing and typesetting industry. Lorem Ipsum has been the industry's standard dummy text ever since the 1500s</p>
    <p>Lorem Ipsum is simply dummy text of the printing and typesetting industry. Lorem Ipsum has been the industry's standard dummy text ever since the 1500s</p>
  </div>
</section>

<footer>
  <div class="abs footer">
    <div class="abs f-brand">Orvane</div>
    <div class="abs" style="left:175px;top:193px;display:flex;gap:24px"><span class="soc"></span><span class="soc"></span><span class="soc"></span></div>
    <div class="abs col" style="left:414px;top:62px">
      <h4 style="margin-bottom:16px">Contact Us</h4>
      <div class="row"><svg width="14" height="18" viewBox="0 0 14 18" style="margin-top:3px"><path d="M7 17s6-6 6-10A6 6 0 001 7c0 4 6 10 6 10z" fill="none" stroke="#fff" stroke-width="1.5"/><circle cx="7" cy="7" r="2" fill="#fff"/></svg><span>27 Harlow Lane<br>Address 40812 TX</span></div>
      <div class="row"><svg width="16" height="16" viewBox="0 0 24 24" style="margin-top:3px"><path d="M6.6 10.8a15 15 0 006.6 6.6l2.2-2.2a1 1 0 011-.25 11.4 11.4 0 003.6.57 1 1 0 011 1V20a1 1 0 01-1 1A17 17 0 013 4a1 1 0 011-1h3.5a1 1 0 011 1c0 1.25.2 2.45.57 3.57a1 1 0 01-.25 1z" fill="#fff"/></svg><span>+49 (0) 987650432</span></div>
      <div class="row"><svg width="16" height="12" viewBox="0 0 16 12" style="margin-top:6px"><rect x="1" y="1" width="14" height="10" fill="none" stroke="#fff" stroke-width="1.4"/><path d="M1 1l7 6 7-6" fill="none" stroke="#fff" stroke-width="1.4"/></svg><span>name@orvane-mail.com</span></div>
    </div>
    <div class="abs col" style="left:642px;top:62px">
      <h4 style="margin-bottom:14px">Company</h4>
      Home<br>Gearboxes &amp; Motors<br>Engine Components<br>Drawing Parts<br>Machines &amp; Accessories
    </div>
    <div class="abs col" style="left:862px;top:64px;width:250px">
      <h4 style="margin-bottom:14px">Stil have questions?</h4>
      A repesentative will aswer your questions as soon as possible.
    </div>
    <div class="abs contact-now"><span class="ic"><svg width="16" height="16" viewBox="0 0 24 24"><path d="M6.6 10.8a15 15 0 006.6 6.6l2.2-2.2a1 1 0 011-.25 11.4 11.4 0 003.6.57 1 1 0 011 1V20a1 1 0 01-1 1A17 17 0 013 4a1 1 0 011-1h3.5a1 1 0 011 1c0 1.25.2 2.45.57 3.57a1 1 0 01-.25 1z" fill="none" stroke="#fff" stroke-width="1.6"/></svg></span>Contact Now</div>
  </div>
  <div class="abs bottombar">
    <span class="abs" style="left:142px;top:34px">Copyright 2020 Orvane. All Rights Reserved.</span>
    <span class="abs" style="left:840px;top:36px;font-size:14px">Privacy Policy &nbsp;&nbsp;|&nbsp;&nbsp; Terms Of Services</span>
  </div>
</footer>

</body>
</html>
```